All Natural Mosquito Repellent

My company, BrightFern Company has created an all natural mosquito repellent. I already have other all natural products that I have developed and created labels for. I will include a copy of that label so you have something to work from. I will need two labels. One for the front of the bottle and one for the back. The back label will need space for a UPC. The labels need to be 63mm (H) x 39mm (W)

Target Market(s)

Consumers, Organic, People who like natural products

Font styles to use
Other font styles liked:
• A combination of both Serif and Sans Serif

Requirements
Must have
• Use the words Organic, All Natural, Travel size, made in the USA label
Nice to have
• tag line: Don't beat them off. Spray them away.

```html
<!DOCTYPE html>
<html lang="en">
<head>
<meta charset="utf-8">
<title>BrightFern Co. — Mosquito Repellent Labels</title>
<link href="https://fonts.googleapis.com/css2?family=Alfa+Slab+One&family=Roboto+Condensed:wght@400;700&family=Montserrat:wght@500;600&family=Kalam:wght@400&display=swap" rel="stylesheet">
<style>
  :root {
    --bg: #f7df91;
    --wood: #e9b534;
    --wood-light: #f0c448;
    --charcoal: #444446;
    --charcoal-deep: #3a3a3c;
    --leaf: #4f8a34;
    --teal: #2a9d7c;
    --rust: #d8662f;
    --ink: #4b4a48;
    --white: #ffffff;
    --sun: #e98f2a;
  }
  * { box-sizing: border-box; margin: 0; padding: 0; }
  html, body { width: 1200px; height: 1121px; overflow: hidden; }
  body { background: var(--bg); position: relative; font-family: "Roboto Condensed", sans-serif; color: var(--ink); }

  .label {
    position: absolute;
    display: flex; flex-direction: column; align-items: center;
    background: linear-gradient(180deg, var(--wood-light), var(--wood));
    text-align: center;
    overflow: hidden;
  }
  .tab {
    font-family: "Montserrat", sans-serif; font-weight: 600;
    color: var(--white); letter-spacing: 0.08em;
    display: flex; align-items: center; justify-content: center;
  }
  .title {
    font-family: "Alfa Slab One", serif; line-height: 1;
    letter-spacing: 0.02em;
  }
  .title .star { color: var(--rust); font-size: 0.6em; vertical-align: middle; }
  .tagline { font-weight: 700; letter-spacing: 0.08em; text-transform: uppercase; }
  .badge { border-radius: 50%; background: var(--sun); }
  .brand-name { font-family: "Roboto Condensed", sans-serif; font-weight: 700; color: var(--ink); letter-spacing: 0.02em; }
  .crafted { font-family: "Kalam", cursive; color: var(--ink); }
  .claims { font-family: "Montserrat", sans-serif; font-weight: 600; letter-spacing: 0.18em; text-transform: uppercase; }
  .footer { position: absolute; left: 0; right: 0; display: flex; justify-content: space-between; align-items: flex-end; padding: 0 14px; }
  .made-usa { display: flex; flex-direction: column; align-items: center; gap: 1px; font-size: 3px; font-weight: 700; letter-spacing: 0.05em; }
  .volume { font-size: 6px; font-weight: 700; }

  /* Label one: yellow with charcoal frame */
  .label-framed { left: 61px; top: 186px; width: 196px; height: 315px; border: 5px solid var(--charcoal); }
  .label-framed .tab { background: var(--leaf); width: 92px; height: 29px; font-size: 9px; }
  .label-framed .title { color: var(--white); margin-top: 14px; font-size: 22px; }
  .label-framed .title-sub { color: var(--white); font-size: 14px; margin-top: 2px; }
  .label-framed .tagline { font-size: 6px; margin-top: 14px; }
  .label-framed .badge { width: 70px; height: 70px; margin-top: 12px; }
  .label-framed .brand-name { font-size: 15px; margin-top: 6px; }
  .label-framed .crafted { font-size: 7px; margin-top: 0; }
  .label-framed .claims { font-size: 6px; line-height: 12px; margin-top: 8px; }
  .label-framed .footer { bottom: 10px; }

  /* Label two: charcoal with yellow core */
  .label-dark { left: 644px; top: 175px; width: 196px; height: 315px; background: var(--charcoal-deep); }
  .label-dark .accent-strip { position: absolute; top: 0; left: 53px; width: 90px; height: 4px; background: var(--rust); }
  .label-dark .tab { background: var(--teal); width: 90px; height: 27px; margin-top: 4px; font-size: 8px; color: #1c5f4b; }
  .label-dark .title { color: var(--wood); font-size: 22px; margin-top: 10px; }
  .label-dark .title-sub { color: var(--wood); font-size: 19px; margin-top: 3px; }
  .label-dark .band { width: 100%; background: var(--rust); color: var(--white); font-size: 6px; padding: 3px 0; }
  .label-dark .tagline-band { margin-top: 9px; }
  .label-dark .core { width: 100%; background: linear-gradient(180deg, var(--wood-light), var(--wood)); display: flex; flex-direction: column; align-items: center; padding: 8px 0 6px; }
  .label-dark .badge { width: 66px; height: 66px; }
  .label-dark .brand-name { font-size: 15px; margin-top: 6px; }
  .label-dark .crafted { font-size: 7px; }
  .label-dark .claims-band { letter-spacing: 0.12em; font-size: 6px; }
  .label-dark .footer { bottom: 10px; color: var(--white); }
  .label-dark .made-usa { color: var(--white); }

  /* Label three: open yellow */
  .label-open { left: 315px; top: 709px; width: 228px; height: 294px; }
  .label-open .tab { background: var(--teal); width: 104px; height: 32px; font-size: 10px; }
  .label-open .title { color: var(--white); font-size: 26px; margin-top: 10px; }
  .label-open .title-sub { color: var(--white); font-size: 17px; margin-top: 2px; }
  .label-open .tagline { font-size: 7px; margin-top: 9px; }
  .label-open .badge { width: 76px; height: 76px; margin-top: 10px; }
  .label-open .brand-name { font-size: 17px; margin-top: 6px; }
  .label-open .crafted { font-size: 8px; }
  .label-open .band { width: 100%; background: var(--rust); color: var(--white); font-size: 7px; padding: 2px 0; margin-top: 10px; letter-spacing: 0.12em; }
  .label-open .footer { bottom: 10px; padding: 0 24px; }
</style>
</head>
<body>

  <!-- Option one -->
  <section class="label label-framed" aria-label="Front label, framed version">
    <div class="tab">ALL NATURAL</div>
    <h1 class="title">MOSQUITO</h1>
    <div class="title title-sub"><span class="star">★</span> REPELLENT <span class="star">★</span></div>
    <p class="tagline">Don't beat them off. Spray them away</p>
    <div class="badge" aria-hidden="true"></div>
    <div class="brand-name">BRIGHTFERN CO.</div>
    <div class="crafted">crafted by hand, with love ★ in the U.S.A.</div>
    <p class="claims">Organic<br>All Natural<br>Travel Size</p>
    <div class="footer">
      <div class="made-usa">
        <svg width="17" height="11" viewBox="0 0 17 11" aria-hidden="true"><rect width="17" height="11" fill="#4b4a48"/><rect x="0" y="2" width="17" height="1" fill="#e9b534"/><rect x="0" y="5" width="17" height="1" fill="#e9b534"/><rect x="0" y="8" width="17" height="1" fill="#e9b534"/></svg>
        MADE IN THE USA
      </div>
      <div class="volume">4oz &nbsp;|&nbsp; 118ml</div>
    </div>
  </section>

  <!-- Option two -->
  <section class="label label-dark" aria-label="Front label, charcoal version">
    <div class="accent-strip"></div>
    <div class="tab">ALL NATURAL</div>
    <h1 class="title">MOSQUITO</h1>
    <div class="title title-sub">REPELLENT</div>
    <p class="band tagline tagline-band">Don't beat them off. Spray them away</p>
    <div class="core">
      <div class="badge" aria-hidden="true"></div>
      <div class="brand-name">BRIGHTFERN CO.</div>
      <div class="crafted">crafted by hand, with love ★ in the U.S.A.</div>
    </div>
    <p class="band claims claims-band">Organic &nbsp;|&nbsp; All Natural &nbsp;|&nbsp; Travel Size</p>
    <div class="footer">
      <div class="made-usa">
        <svg width="17" height="11" viewBox="0 0 17 11" aria-hidden="true"><rect width="17" height="11" fill="#ffffff"/><rect x="0" y="2" width="17" height="1" fill="#3a3a3c"/><rect x="0" y="5" width="17" height="1" fill="#3a3a3c"/><rect x="0" y="8" width="17" height="1" fill="#3a3a3c"/></svg>
        MADE IN THE USA
      </div>
      <div class="volume">4oz &nbsp;|&nbsp; 118ml</div>
      <div style="width:17px"></div>
    </div>
  </section>

  <!-- Option three -->
  <section class="label label-open" aria-label="Front label, open version">
    <div class="tab">ALL NATURAL</div>
    <h1 class="title">MOSQUITO</h1>
    <div class="title title-sub"><span class="star">★</span>REPELLENT<span class="star">★</span></div>
    <p class="tagline">Don't beat them off. Spray them away</p>
    <div class="badge" aria-hidden="true"></div>
    <div class="brand-name">BRIGHTFERN CO.</div>
    <div class="crafted">crafted by hand, with love ★ in the U.S.A.</div>
    <p class="band claims">Organic &nbsp;|&nbsp; All Natural &nbsp;|&nbsp; Travel Size</p>
    <div class="footer">
      <div class="made-usa">
        <svg width="19" height="12" viewBox="0 0 19 12" aria-hidden="true"><rect width="19" height="12" fill="#4b4a48"/><rect x="0" y="2" width="19" height="1" fill="#e9b534"/><rect x="0" y="5" width="19" height="1" fill="#e9b534"/><rect x="0" y="8" width="19" height="1" fill="#e9b534"/></svg>
        MADE IN THE USA
      </div>
      <div class="volume">4oz &nbsp;|&nbsp; 118ml</div>
    </div>
  </section>

</body>
</html>
```